FernlowCo - Business Card and Letterhead

After having received some fantastic submissions in our recent logo design project, I would now like to extend our branding to letterheads and business cards.
FernlowCo is a consulting service in the Construction Industry. We deal with both residential and commercial projects, and our clients include Architects, Builders, Tradespeople and Home Owners.
The designs should be simple and effective, convey personal service and professionalism, and display some level of creativity.
For both the business cards and letterhead, a white card stock will be used. This project is for business cards and letterheads only. Our new logo is attached for use.
The designs should incorporate our two main colours which are Blue (RGB 14,92,143) and Green (RGB 132,194,37).
For the time being, please submit all designs showing generic information including name, mobile number, email, postal address and website details. No fax number or physical address is required. I will provide our actual contact details once a final design has been selected.
I encourage you to interpret this brief in your own creative way, and look forward to some quality submissions.
Thanks!
Leo
FernlowCo.

```html
<!DOCTYPE html>
<html lang="en">
<head>
<meta charset="utf-8">
<title>FernlowCo – Letterhead and Business Cards</title>
<link href="https://fonts.googleapis.com/css2?family=PT+Sans:wght@400;700&display=swap" rel="stylesheet">
<style>
  :root {
    --blue: #0e5c8f;
    --navy: #0d4a84;
    --green: #84c225;
    --ink: #1c1c1c;
    --muted: #444;
    --paper: #ffffff;
    --backdrop: #eceef0;
  }
  * { box-sizing: border-box; margin: 0; padding: 0; }
  html, body { width: 1200px; height: 900px; overflow: hidden; }
  body {
    background: var(--backdrop);
    font-family: "PT Sans", Arial, sans-serif;
    color: var(--ink);
    position: relative;
  }

  /* Letterhead */
  .letterhead {
    position: absolute; left: 258px; top: 109px;
    width: 472px; height: 678px;
    background: var(--paper);
    box-shadow: 0 2px 8px rgba(0,0,0,.12);
  }
  .brand {
    display: flex; align-items: center; gap: 6px;
    font-weight: 700; color: var(--blue);
  }
  .brand-square { background: var(--green); display: block; }
  .letterhead .brand { position: absolute; left: 41px; top: 30px; font-size: 23px; }
  .letterhead .brand-square { width: 18px; height: 18px; }

  .letter {
    position: absolute; left: 44px; top: 172px; width: 380px;
    font-size: 11.4px; line-height: 13.6px; color: var(--ink);
  }
  .letter p { text-align: justify; }
  .letter .date-address { margin-bottom: 13.6px; text-align: left; }
  .letter .closing { margin-top: 13.6px; }
  .signature {
    display: block; width: 110px; height: 26px; margin-top: 16px;
    background: linear-gradient(90deg, #f1f1f1, #e4e4e4);
  }
  .signer-title { font-size: 12px; margin-top: 2px; }

  .letter-footer {
    position: absolute; left: 28px; top: 628px;
    display: flex; gap: 12px; font-size: 7.2px; line-height: 9.5px; color: var(--muted);
  }
  .letter-footer .divider { width: 1px; background: #bbb; }
  .contact-line { display: flex; align-items: center; gap: 6px; }
  .icon { width: 7px; height: 7px; flex: none; }
  .footer-block {
    position: absolute; right: 14px; top: 617px; width: 78px; height: 40px;
    background: var(--green);
  }
  .footer-rule { position: absolute; left: 0; right: 0; top: 657px; height: 4px; background: var(--green); }
  .footer-band { position: absolute; left: 0; right: 0; top: 663px; height: 15px; background: var(--navy); }

  /* Business card front */
  .card {
    position: absolute; width: 213px; height: 122px;
    box-shadow: 0 2px 6px rgba(0,0,0,.14);
  }
  .card-front {
    left: 826px; top: 302px; background: var(--navy);
    display: flex; flex-direction: column; align-items: center; justify-content: center; gap: 8px;
  }
  .card-front .brand { color: #fff; font-size: 14px; flex-direction: column; gap: 8px; }
  .card-front .brand-square { width: 30px; height: 30px; }

  /* Business card back */
  .card-back { left: 831px; top: 457px; background: var(--paper); }
  .card-back .brand { position: absolute; left: 16px; top: 14px; font-size: 13px; gap: 4px; }
  .card-back .brand-square { width: 10px; height: 10px; }
  .holder { position: absolute; right: 12px; top: 54px; text-align: right; }
  .holder-name { font-size: 7.5px; font-weight: 700; letter-spacing: .2px; }
  .holder-title { font-size: 6.5px; color: var(--green); }
  .holder-rule { position: absolute; left: 16px; right: 12px; top: 74px; height: 1px; background: var(--blue); }
  .card-contacts {
    position: absolute; left: 16px; top: 78px; font-size: 5.4px; line-height: 6.4px; color: var(--muted);
  }
  .card-contacts .contact-line { gap: 3px; }
  .card-contacts .icon { width: 4px; height: 4px; }
  .card-block { position: absolute; right: 4px; top: 98px; width: 34px; height: 16px; background: var(--green); }
  .card-rule { position: absolute; left: 0; right: 0; top: 113px; height: 3px; background: var(--green); }
  .card-band { position: absolute; left: 0; right: 0; top: 117px; height: 5px; background: var(--navy); }
</style>
</head>
<body>

<section class="letterhead" aria-label="Letterhead">
  <div class="brand"><span class="brand-square"></span>FernlowCo</div>

  <div class="letter">
    <p class="date-address">November 1, 2012<br>Mr. Martin Hale<br>88 Quarry Lane<br>Bristol, U.K 45210</p>
    <p>Dear Mr. Hale</p>
    <p>The first paragraph of a typical business letter is used to state the main point of the letter. Begin with a friendly opening; then quickly transition into the purpose of your letter. Use a couple of sentences to explain the purpose, but do not go in to detail until the next paragraph.</p>
    <p>Beginning with the second paragraph, state the supporting details to justify your purpose. These may take the form of background information, statistics or first-hand accounts. A few short paragraphs within the body of the letter should be enough to support your reasoning.</p>
    <p>Finally, in the closing paragraph, briefly restate your purpose and why it is important. If the purpose of your letter is related to your employment, consider ending your letter with your contact information and title if it not included on letterhead. However, if the purpose is informational, think about closing with gratitude for the reader’s time.</p>
    <p class="closing">Sincerely,</p>
    <span class="signature" role="img" aria-label="Handwritten signature of Owen Price"></span>
    <p class="signer-title">President</p>
  </div>

  <div class="letter-footer">
    <div>17 Harbour Row,<br>Suite 40, Newport, MA 01920</div>
    <div class="divider"></div>
    <div>
      <div class="contact-line"><svg class="icon" viewBox="0 0 10 10"><path d="M2 1l2 2-1 1.5c.8 1.5 1.8 2.5 3.5 3.5L8 6.5l2 2L8.5 10C4 9 1 6 0 1.5z" fill="#84c225"/></svg>999-999-9999</div>
      <div class="contact-line"><svg class="icon" viewBox="0 0 10 10"><rect x="1" y="2" width="8" height="7" rx="1" fill="#84c225"/></svg>999-999-9999</div>
    </div>
    <div class="divider"></div>
    <div>
      <div class="contact-line"><svg class="icon" viewBox="0 0 10 10"><rect x="0" y="2" width="10" height="6" fill="#84c225"/></svg>hello@fernlowco.com</div>
      <div class="contact-line"><svg class="icon" viewBox="0 0 10 10"><circle cx="5" cy="5" r="4.5" fill="#84c225"/></svg>www.fernlowco.com</div>
    </div>
  </div>
  <div class="footer-block"></div>
  <div class="footer-rule"></div>
  <div class="footer-band"></div>
</section>

<section class="card card-front" aria-label="Business card front">
  <div class="brand"><span class="brand-square"></span>FernlowCo</div>
</section>

<section class="card card-back" aria-label="Business card back">
  <div class="brand"><span class="brand-square"></span>FernlowCo</div>
  <div class="holder">
    <div class="holder-name">NOAH REED</div>
    <div class="holder-title">President</div>
  </div>
  <div class="holder-rule"></div>
  <div class="card-contacts">
    <div>17 Harbour Row Ste 4, Nelson NZ 7010</div>
    <div class="contact-line"><svg class="icon" viewBox="0 0 10 10"><circle cx="5" cy="5" r="5" fill="#84c225"/></svg>999-999-9999</div>
    <div class="contact-line"><svg class="icon" viewBox="0 0 10 10"><circle cx="5" cy="5" r="5" fill="#84c225"/></svg>999-999-9999</div>
    <div class="contact-line"><svg class="icon" viewBox="0 0 10 10"><circle cx="5" cy="5" r="5" fill="#84c225"/></svg>noah@fernlowco.com</div>
    <div class="contact-line"><svg class="icon" viewBox="0 0 10 10"><circle cx="5" cy="5" r="5" fill="#84c225"/></svg>www.fernlowco.com</div>
  </div>
  <div class="card-block"></div>
  <div class="card-rule"></div>
  <div class="card-band"></div>
</section>

</body>
</html>
```